We require banners for Twitter, LinkedIn and Facebook.

We want 3 banners that reflect the FinTech sector. We provide outsourced sales and marketing services to Fintech companies, mature and startup. See our website at www.corvelasystems.com. We operate in Europe, Middle East , Africa and Asia Pacific. We want the banners similar, highly professional and editable.

Target Market(s)

European and Asia Pacific FinTech sector of existing or start-up companies seeking to engage as an outsourced sales and marketing services provider.

Industry/Entity Type

Marketing

Font styles to use
Sans Serif

Requirements
Must have
• A high tech financial services image
Nice to have
• Fintech infographic, banking systems, financial systems, financial or stock market images
Should not have
• cartoon or drawn images.

```html
<!DOCTYPE html>
<html lang="en">
<head>
<meta charset="UTF-8">
<title>Fintech Outsourced Sales &amp; Marketing Banner</title>
<link rel="stylesheet" href="https://fonts.googleapis.com/css2?family=Open+Sans:wght@600&display=swap">
<style>
  :root {
    --page-bg: #ffffff;
    --banner-dark: #14161d;
    --banner-mid: #242c3f;
    --banner-light: #3a4560;
    --text-light: #ffffff;
    --text-soft: #e6e9ef;
    --button-bg: #23262d;
  }
  html, body {
    margin: 0;
    padding: 0;
    width: 1200px;
    height: 1200px;
    overflow: hidden;
    background: var(--page-bg);
    font-family: "Open Sans", Arial, sans-serif;
  }
  .canvas {
    position: relative;
    width: 1200px;
    height: 1200px;
  }
  .banner {
    position: absolute;
    left: 40px;
    top: 430px;
    width: 1120px;
    height: 340px;
    overflow: hidden;
  }
  .banner-photo {
    position: absolute;
    inset: 0;
    background:
      radial-gradient(ellipse at 78% 25%, rgba(120,135,165,0.45), transparent 55%),
      radial-gradient(ellipse at 30% 85%, rgba(90,100,120,0.35), transparent 50%),
      linear-gradient(90deg, var(--banner-dark) 0%, var(--banner-mid) 55%, var(--banner-light) 100%);
  }
  .banner-content {
    position: absolute;
    inset: 0;
    text-align: center;
    color: var(--text-light);
  }
  .headline {
    position: absolute;
    left: 0;
    right: 0;
    top: 98px;
    margin: 0;
    font-size: 20px;
    font-weight: 600;
    line-height: 34px;
    white-space: nowrap;
  }
  .tagline {
    position: absolute;
    left: 0;
    right: 0;
    top: 184px;
    margin: 0;
    font-size: 15px;
    font-weight: 600;
    color: var(--text-soft);
    white-space: nowrap;
  }
  .cta-button {
    position: absolute;
    left: 434px;
    top: 242px;
    width: 252px;
    height: 44px;
    line-height: 44px;
    background: var(--button-bg);
    color: var(--text-light);
    font-size: 16px;
    font-weight: 600;
    text-decoration: none;
  }
</style>
</head>
<body>
  <div class="canvas">
    <section class="banner">
      <div class="banner-photo" role="img" aria-label="Dark blue-toned photo of hands working with a tablet and laptop beside a coffee cup, overlaid with financial charts and data graphics"></div>
      <div class="banner-content">
        <h1 class="headline">EUROPEAN AND ASIA PACIFIC FINTECH SECTOR OF EXISTING OR START-UP COMPANIES<br>SEEKING TO ENGAGE AS AN OUTSOURCED SALES AND MARKETING SERVICES PROVIDER.</h1>
        <p class="tagline">CONSTANTLY CHALLENGING OURSELVES TO DELIVER MORE TO OUR CLIENTS</p>
        <a class="cta-button" href="#">GET IN TOUCH WITH US</a>
      </div>
    </section>
  </div>
</body>
</html>
```